Medical Staffing Pamphlet

We are starting to staff for Medical positions for the first time, we need pamphlets to take to medical facilities to try to gain new business

Need an copy to edit, many errors.

```html
<!DOCTYPE html>
<html lang="en">
<head>
<meta charset="utf-8">
<title>Keystone Staffing Medical – Pamphlet</title>
<link rel="stylesheet" href="https://fonts.googleapis.com/css2?family=Cinzel:wght@600;700&family=Roboto:wght@400;500&display=swap">
<style>
  :root{
    --navy:#353f73;
    --green:#4e7d3e;
    --white:#ffffff;
    --page:#f3f8fa;
    --photo-a:#dfe9f1;
    --photo-b:#9fb8cf;
    --tagline:#3f7a2e;
    --sans:"Roboto", Arial, sans-serif;
    --serif:"Cinzel", Georgia, serif;
  }
  *{box-sizing:border-box;margin:0;padding:0}
  html,body{width:1200px;height:1200px;overflow:hidden;background:var(--page)}
  .canvas{position:relative;width:1200px;height:1200px}
  .sheet{position:absolute;box-shadow:0 4px 14px rgba(0,0,0,.18);overflow:hidden;background:var(--white)}
  .sheet--outside{left:233px;top:51px;width:703px;height:543px}
  .sheet--inside{left:248px;top:642px;width:680px;height:523px;background:var(--navy)}
  .shapes{position:absolute;inset:0}
  .abs{position:absolute}
  .photo{background:linear-gradient(160deg,var(--photo-a),var(--photo-b))}
  .icon-area{background:linear-gradient(135deg,#e9eef5,#d5dfe9);border-radius:6px}

  /* outside */
  .front-mark{left:10px;top:4px;width:215px;font:400 20px/1.6 var(--sans);color:var(--white);letter-spacing:2px;text-align:center}
  .promise{left:6px;top:350px;width:222px;font:400 15.5px/2.45 var(--sans);color:var(--white);letter-spacing:1.6px;text-align:center;text-transform:uppercase}
  .contact-title{left:243px;top:322px;width:214px;height:62px;display:flex;align-items:center;justify-content:center;font:400 22px/1 var(--sans);color:var(--white);letter-spacing:.5px;transform:rotate(5deg)}
  .address{left:243px;top:420px;width:214px;font:400 16px/1.45 var(--sans);color:var(--white);text-align:center;transform:rotate(-3deg)}
  .cover-title{left:469px;top:295px;width:234px;font:400 35px/1.2 var(--sans);color:var(--white);text-align:center;letter-spacing:1px}
  .tagline{left:469px;top:473px;width:234px;font:400 15px/1.35 var(--sans);color:var(--tagline);text-align:center}

  /* inside */
  .who-tab{left:0;top:28px;width:229px;height:45px;background:var(--white);display:flex;align-items:center;justify-content:center;font:700 19px/1 var(--serif);color:var(--navy);letter-spacing:1px}
  .who-text{left:12px;top:88px;width:205px;font:400 11.2px/1.34 var(--sans);color:var(--white);text-align:center}
  .trust{left:238px;top:68px;width:210px;font:400 14px/2.25 var(--sans);color:var(--white);letter-spacing:1.4px;text-align:center;text-transform:uppercase}
  .trust b{font:600 15px/1 var(--serif);letter-spacing:2px}
  .team-photo{left:0;top:268px;width:453px;height:239px}
  .services{left:453px;top:0;width:227px;height:523px;background:var(--green)}
  .brand-box{left:13px;top:22px;width:200px;height:100px;background:var(--white);display:flex;align-items:center;justify-content:center;gap:10px}
  .brand-box .square{width:28px;height:28px;background:var(--navy);flex:none}
  .brand-box .name{font:500 17px/1.1 var(--sans);color:var(--navy);letter-spacing:.5px;text-transform:uppercase}
  .services-title{left:0;top:140px;width:227px;height:45px;background:var(--white);display:flex;align-items:center;justify-content:center;font:700 19px/1 var(--serif);color:var(--green);letter-spacing:1px}
  .band{left:25px;width:177px;height:37px;background:var(--navy);display:flex;align-items:center;justify-content:center;font:700 14.5px/1 var(--serif);color:var(--white);letter-spacing:1px}
  .band--admin{top:198px}
  .band--clinical{top:368px}
  .role-list{left:26px;list-style:none;color:var(--white);font-family:var(--sans);text-transform:uppercase}
  .role-list li{display:flex;align-items:center;gap:14px}
  .role-list li::before{content:"";width:8px;height:8px;border-radius:50%;background:var(--white);flex:none}
  .role-list--admin{top:241px;font-size:11.3px;letter-spacing:.6px}
  .role-list--admin li{height:24.5px}
  .role-list--clinical{top:412px;font-size:8.8px;letter-spacing:.3px}
  .role-list--clinical li{height:24.5px}
</style>
</head>
<body>
<main class="canvas">

  <!-- Outside of the pamphlet -->
  <section class="sheet sheet--outside">
    <svg class="shapes" viewBox="0 0 703 543" width="703" height="543" aria-hidden="true">
      <polygon points="233,0 469,0 469,292 233,242" fill="var(--navy)"/>
      <polygon points="0,192 469,302 469,330 0,224" fill="var(--navy)"/>
      <polygon points="0,234 469,340 469,366 0,264" fill="var(--green)"/>
      <polygon points="0,274 233,326 233,543 0,543" fill="var(--navy)"/>
      <rect x="243" y="404" width="214" height="125" fill="var(--green)"/>
      <rect x="469" y="168" width="234" height="122" fill="var(--green)"/>
      <polygon points="469,168 703,290 703,465 469,465" fill="var(--navy)"/>
      <rect x="542" y="178" width="92" height="92" fill="var(--white)"/>
    </svg>

    <div class="abs icon-area" style="left:40px;top:40px;width:150px;height:150px" role="img" aria-label="Stethoscope illustration"></div>
    <p class="abs front-mark" style="top:92px;left:233px;width:236px">KEYSTONE STAFFING<br>MEDICAL</p>
    <p class="abs promise">Our medical<br>staffing specialist<br>will provide you<br>quality employees</p>

    <div class="abs contact-title" style="background:var(--navy)">CONTACT US</div>
    <p class="abs address">2450 N. Maple Ridge Rd.<br>Fairview, Indiana 47900<br>812-555-0148</p>

    <div class="abs photo" style="left:469px;top:0;width:234px;height:161px" role="img" aria-label="Photo of a smiling medical team in white coats and scrubs"></div>
    <h1 class="abs cover-title">KEYSTONE<br>STAFFING<br>MEDICAL</h1>
    <p class="abs tagline">Providing high<br>quality healthcare<br>professionals</p>
  </section>

  <!-- Inside of the pamphlet -->
  <section class="sheet sheet--inside">
    <h2 class="abs who-tab">WHO WE ARE</h2>
    <p class="abs who-text">Keystone Staffing is the largest locally owned recruiting company in the TriState. We began building staffing partnerships are the foundation of our success. We provide customized staffing solutions for the many industries we service, including medical.</p>
    <p class="abs trust"><b>Put your trust<br>in us,</b> and we will<br>take care of<br>your medical<br>staffin gneeds.</p>

    <div class="abs photo team-photo" role="img" aria-label="Photo of a group of doctors and nurses with stethoscopes"></div>

    <aside class="abs services">
      <div class="abs brand-box">
        <span class="square"></span>
        <span class="name">Keystone<br>Staffing<br>Services</span>
      </div>
      <h2 class="abs services-title">OUR SERVICES</h2>

      <h3 class="abs band band--admin">ADMINISTRATIVE</h3>
      <ul class="abs role-list role-list--admin">
        <li>Billing specialists</li>
        <li>Coding specialists</li>
        <li>Medical records</li>
        <li>Office managers</li>
        <li>Receptionists</li>
      </ul>

      <h3 class="abs band band--clinical">CLINICAL</h3>
      <ul class="abs role-list role-list--clinical">
        <li>Certified medical assistants</li>
        <li>Registered medical assistants</li>
        <li>Certified nursing assistants</li>
        <li>Phlebotomists</li>
      </ul>
    </aside>
  </section>

</main>
</body>
</html>
```